Very new and innovative Web design for Property managers of Vacation rentals

We are looking for a new website design for travel agencies and property managers specialised on vacation rentals business, holiday villas and apartments.

The end users of this website are travellers who are looking for a vacation home for their next holiday: this is the reason why the website must be easy to use, attractive, professional, possibly elegant and focused on get new reservations.

This is a draft of our current website: https://demo5.lunquora.com/
Please consider that we would like to have proposals with a totally different and innovative layout, surprise us!

These are the pages of the website:
• Homepage: feel free to redesign all the homepage as you wish, surprise us with something very new! Please consider that Property manager/Travel agencies usually want to have the opportunity to put in evidence groups of houses with specific characteristics (eg. villas with private swimming pool, apartment in big/small towns, villas with air co, etc…), destinations and tourist areas, and sometimes experiences or activities (please consider that the website layout must be suitable even if some of the previous sections are not used).
• Search page: we’d like to organise the results of the search page in three different ways:
o Grid
o Map
o List
• Property page: to illustrate the characteristics, descriptions, images, …. of the property. It is very important to put in evidence images of the property and to maintain the booking form (and the other call to action bottom – eg. whatsapp) always visible
• Custom pages: static pages composed usually by text, images and call to actions
• Contact us (general form)
• Info request (specific of a property form)
• Booking process
• Blog, organised in four pages:
o Home Page – introduction to the blog
o List of articles
o Single article
o Site Map (presentation of categories and sub-categories)

If possible, we’d prefer to receive the material in Adobe XD or similar so that we can obtain the three versions:
- smartphone
- tablet
- desktop

The website will be then developed in Bootstrap: as a result we’ll need the icons in SVG format (or the library used)

In attachment you can find the map of the website pages

```html
<!DOCTYPE html>
<html lang="en">
<head>
<meta charset="utf-8">
<title>Villaroute – Vacation Rentals</title>
<link rel="stylesheet" href="https://fonts.googleapis.com/css2?family=Poppins:wght@300;400;500;600&family=Bebas+Neue&family=Great+Vibes&display=swap">
<style>
:root{
  --green:#17b57f;
  --green-dark:#0f9a6b;
  --orange:#f7894a;
  --teal:#2c4a55;
  --navy:#0f2b36;
  --navy-deep:#163b48;
  --ink:#1d2a30;
  --muted:#5b6a70;
  --line:#c9d2d5;
  --white:#ffffff;
}
*{box-sizing:border-box;margin:0;padding:0}
html,body{width:1200px;height:3764px;overflow:hidden}
body{position:relative;background:var(--white);font-family:'Poppins',sans-serif;color:var(--ink)}
h2,h3,h4{font-weight:400}
.abs{position:absolute}
.btn{position:absolute;display:flex;align-items:center;justify-content:center;border-radius:20px;color:var(--white);font-size:10px;font-weight:500}
.btn-orange{background:var(--orange)}
.btn-green{background:var(--green)}
.section-title{position:absolute;left:311px;font-size:24px;font-weight:400;letter-spacing:.5px;color:var(--ink)}
.rule{position:absolute;left:294px;width:120px;height:1px;background:var(--line)}
.lead{position:absolute;left:431px;width:460px;font-size:11px;line-height:15px;color:var(--muted)}
.photo{position:absolute}
/* header */
.brand{position:absolute;left:105px;top:30px;display:flex;align-items:center;gap:8px;font-size:26px;font-weight:500;color:var(--ink)}
.brand-mark{width:26px;height:26px;background:var(--green);border-radius:50%}
.call{left:838px;top:20px;font-size:13px;font-family:'Bebas Neue',sans-serif;letter-spacing:.5px;color:var(--ink)}
.call b{color:var(--green);font-weight:400}
.social{position:absolute;width:22px;height:22px;border:1.5px solid var(--green);border-radius:50%}
.nav{position:absolute;top:58px;left:527px;display:flex;gap:25px;font-size:10.5px;font-weight:500;color:var(--ink)}
.nav .active{color:var(--green)}
/* hero */
.hero-photo{left:0;top:94px;width:1200px;height:520px;background:linear-gradient(180deg,#9fc2dc 0%,#c9dbe6 35%,#b9a78f 60%,#6f8d9a 80%,#4f6f7b 100%)}
.hero-band{left:0;width:1200px;background:var(--green)}
.tag{left:199px;top:212px;width:181px;height:22px;background:var(--green);color:#fff;font-family:'Bebas Neue',sans-serif;font-size:15px;padding:3px 12px;letter-spacing:.5px}
.hero-head{left:199px;top:256px;font-family:'Bebas Neue',sans-serif;font-size:40px;line-height:38px;color:#111;letter-spacing:.5px;white-space:nowrap}
.hero-head .script{display:inline-block;font-family:'Great Vibes',cursive;color:var(--orange);font-size:68px;line-height:0;letter-spacing:0;margin:0 14px 0 16px;vertical-align:-4px}
.hero-text{left:199px;top:342px;width:300px;font-size:11px;line-height:14px;color:#111;font-weight:500}
.hero-script{left:0;width:1200px;top:548px;text-align:center;font-family:'Great Vibes',cursive;font-size:40px;color:#fff}
.field{position:absolute;top:680px;height:36px;background:#fff;border-radius:20px;display:flex;align-items:center;padding:0 20px;font-size:9px;color:var(--muted);gap:10px}
.field .chev{margin-left:auto;width:6px;height:6px;border-right:1.3px solid var(--muted);border-bottom:1.3px solid var(--muted);transform:rotate(45deg) translateY(-2px)}
/* features */
.feature{position:absolute;top:943px;width:130px}
.feature svg{display:block;width:40px;height:40px}
.feature p{margin-top:16px;font-size:12px;line-height:14px;font-weight:500;color:var(--ink)}
/* villa slider */
.teal-band{left:0;top:1232px;width:1200px;height:563px;background:var(--teal)}
.villa-card{position:absolute;top:1139px;width:251px;height:187px}
.villa-label{position:absolute;top:153px;left:25px;width:157px;height:66px;background:var(--green);color:#fff;padding:14px 19px;font-size:14px;font-weight:500;line-height:16px}
.villa-label small{display:block;font-size:9px;font-weight:500}
.arrow-circle{position:absolute;width:24px;height:24px;border-radius:50%;border:1.3px solid var(--green);background:#fff;display:flex;align-items:center;justify-content:center}
.arrow-circle svg{width:10px;height:10px}
/* testimonial */
.testi-title{left:0;width:1200px;top:1418px;text-align:center;color:#fff;font-size:23px;font-weight:400;letter-spacing:.5px}
.avatar{left:554px;top:1502px;width:90px;height:90px;border-radius:50%;border:3px solid var(--green);background:linear-gradient(135deg,#f3c7a3,#c98a5c)}
.quote{left:260px;width:680px;top:1609px;text-align:center;font-style:italic;font-size:11px;line-height:19px;color:#fff;font-weight:300}
.dot{position:absolute;top:1721px;width:11px;height:11px;border-radius:50%;border:1px solid #fff}
/* destinations */
.dest{position:absolute;top:1940px;width:182px}
.dest .img{height:248px}
.dest .name{position:relative;margin-top:12px;padding-left:12px;font-size:12px;font-weight:500;color:var(--ink)}
.dest .tab{position:absolute;right:-12px;top:230px;width:25px;height:44px;background:var(--green)}
/* new villas */
.navy-band{left:0;top:2334px;width:1200px;height:579px;background:var(--navy)}
.rental{position:absolute;top:2502px;width:279px;color:#fff}
.rental .img{height:133px;position:relative}
.rental .stars{position:absolute;left:0;top:0;background:var(--orange);padding:2px 6px;font-size:9px;letter-spacing:1px;color:#fff}
.rental h3{margin-top:18px;font-size:13px;font-weight:600}
.rental .desc{margin-top:10px;font-size:9px;line-height:13px;font-weight:300;width:260px}
.specs{margin-top:16px;font-size:9.5px;line-height:19px}
.specs div{display:flex}
.specs span{display:inline-block;width:85px;color:var(--green)}
/* articles */
.article{position:absolute;top:3074px;width:251px}
.article .img{height:162px}
.article .box{position:absolute;left:22px;top:126px;width:209px;height:140px;background:#fff;box-shadow:0 3px 12px rgba(0,0,0,.08);padding:14px 16px}
.article .meta{font-family:'Bebas Neue',sans-serif;font-size:11px;color:var(--ink);letter-spacing:.3px}
.article h4{margin-top:8px;font-size:11px;line-height:14px;font-weight:600}
.article p{margin-top:10px;font-size:8.5px;line-height:13px;color:var(--muted)}
/* footer */
.footer-dark{left:0;width:1200px;background:var(--navy)}
.foot-h{position:absolute;top:3533px;font-size:12px;font-weight:500;color:#fff}
.foot-t{position:absolute;font-size:10px;line-height:18.5px;color:#fff;font-weight:300}
.bottom-bar{left:0;top:3712px;width:1200px;height:52px;background:var(--navy-deep)}
.to-top{left:1080px;top:3726px;width:24px;height:24px}
</style>
</head>
<body>

<!-- Header -->
<div class="brand"><span class="brand-mark"></span>Villaroute</div>
<div class="abs call"><b>CALL US:</b> <svg width="11" height="11" viewBox="0 0 24 24" style="vertical-align:-1px"><path d="M6 2l4 4-2 3c1 3 4 6 7 7l3-2 4 4-3 4C10 22 2 14 2 5z" fill="none" stroke="#17b57f" stroke-width="2"/></svg> +39 055 4827190</div>
<span class="social" style="left:1009px;top:17px"></span>
<span class="social" style="left:1039px;top:17px"></span>
<span class="social" style="left:1069px;top:17px"></span>
<nav class="nav"><span class="active">-- Home --</span><span>About Us</span><span>Special Offers</span><span>Experience</span><span>Blog</span><span>Contact Us</span></nav>
<div class="btn btn-green" style="left:994px;top:54px;width:99px;height:23px">Book Now!</div>

<!-- Hero -->
<div class="photo hero-photo abs" role="img" aria-label="Venice waterfront with a domed basilica, gondolas and blue sky"></div>
<svg class="abs" style="left:0;top:540px" width="1200" height="80" viewBox="0 0 1200 80" preserveAspectRatio="none"><path d="M0 10 C300 40 520 40 760 30 C950 22 1080 10 1200 0 L1200 80 L0 80Z" fill="#17b57f"/></svg>
<div class="abs hero-band" style="top:600px;height:178px"></div>
<div class="abs tag">SUMMER 2021</div>
<div class="abs hero-head">TAKE<span class="script">Your</span>HOLIDAY<br>TO THE NEXT LEVEL</div>
<div class="abs hero-text">Lorem Ipsum is simply dummy text of the printing and typesetting orem Ipsum has been</div>
<div class="btn btn-orange" style="left:199px;top:392px;width:99px;height:23px">Book Now!</div>
<div class="abs hero-script">Exclusive Villas in Italy</div>
<div class="arrow-circle" style="left:587px;top:608px;width:27px;height:27px;border-color:#fff;background:rgba(255,255,255,.3)"><svg viewBox="0 0 10 10"><path d="M2 3.5l3 3 3-3" fill="none" stroke="#fff" stroke-width="1.5"/></svg></div>

<div class="field" style="left:199px;width:156px">▣ Destination<span class="chev"></span></div>
<div class="field" style="left:368px;width:157px">▦ Check In<span class="chev"></span></div>
<div class="field" style="left:538px;width:156px">▦ Check Out<span class="chev"></span></div>
<div class="field" style="left:706px;width:156px">● Travelers<span class="chev"></span></div>
<div class="btn btn-orange" style="left:874px;top:680px;width:124px;height:36px;font-family:'Great Vibes',cursive;font-size:18px;font-weight:400">Search</div>

<!-- Safety -->
<h2 class="section-title" style="top:834px">Safety in Your Holiday Home!</h2>
<div class="rule" style="top:886px"></div>
<p class="lead" style="top:881px">Lorem ipsum dolor sit amet, consectetur adipiscing elit, sed do eiusmod tempor incididunt ut labore et dolore magna aliqua.</p>

<div class="feature" style="left:311px"><svg viewBox="0 0 40 40"><path d="M4 20L20 5l16 15" fill="none" stroke="#f7894a" stroke-width="3"/><path d="M9 18v18h22V18" fill="#17b57f"/><rect x="17" y="24" width="6" height="12" fill="#fff"/></svg><p>Privacy in your<br>holiday home</p></div>
<div class="feature" style="left:460px"><svg viewBox="0 0 40 40"><circle cx="13" cy="8" r="4" fill="#f7894a"/><circle cx="27" cy="8" r="4" fill="#f7894a"/><rect x="8" y="14" width="10" height="14" rx="2" fill="#17b57f"/><rect x="22" y="14" width="10" height="14" rx="2" fill="#17b57f"/><rect x="9" y="28" width="3" height="10" fill="#17b57f"/><rect x="28" y="28" width="3" height="10" fill="#17b57f"/></svg><p>Freedom and<br>independence</p></div>
<div class="feature" style="left:611px"><svg viewBox="0 0 40 40"><rect x="10" y="16" width="12" height="22" rx="3" fill="#17b57f"/><rect x="12" y="8" width="8" height="8" fill="#f7894a"/><path d="M20 9h8" stroke="#17b57f" stroke-width="2"/><circle cx="32" cy="6" r="1.5" fill="#f7894a"/><circle cx="34" cy="11" r="1.5" fill="#f7894a"/></svg><p>Quality controlled<br>cleaning</p></div>
<div class="feature" style="left:759px"><svg viewBox="0 0 40 40"><circle cx="27" cy="12" r="8" fill="none" stroke="#17b57f" stroke-width="3"/><path d="M21 18L6 33l4 4 3-3-2-2 3-2" fill="none" stroke="#17b57f" stroke-width="3"/><path d="M12 6l6 6" stroke="#f7894a" stroke-width="3"/></svg><p>Safe hand-over of<br>the key on-site</p></div>
<div class="btn btn-orange" style="left:313px;top:1051px;width:101px;height:23px">Book Now!</div>

<!-- Villa types -->
<div class="abs teal-band"></div>
<div class="villa-card" style="left:199px"><div class="photo" style="inset:0;background:linear-gradient(180deg,#7d88b6,#c6b7c6 45%,#5c4a3e 75%,#3b2f29)" role="img" aria-label="Lagoon villa deck with daybed over the sea at sunset"></div><div class="villa-label">Lagoon<small>Villa</small></div></div>
<div class="villa-card" style="left:475px"><div class="photo" style="inset:0;background:linear-gradient(180deg,#5aa0da,#bcd8ee 40%,#e8ecee 60%,#5e9a4a)" role="img" aria-label="Modern white garden villa with pool and lawn"></div><div class="villa-label">Garden<small>Villa</small></div></div>
<div class="villa-card" style="left:750px"><div class="photo" style="inset:0;background:linear-gradient(180deg,#2f6fb4,#8fbbe0 35%,#6c7a52 55%,#2d3c3e)" role="img" aria-label="Deluxe pool villa with loungers by the water"></div><div class="villa-label">Deluxe Pool<small>Villa</small></div></div>
<div class="arrow-circle" style="left:187px;top:1220px"><svg viewBox="0 0 10 10"><path d="M6.5 2l-3 3 3 3" fill="none" stroke="#17b57f" stroke-width="1.5"/></svg></div>
<div class="arrow-circle" style="left:987px;top:1220px"><svg viewBox="0 0 10 10"><path d="M3.5 2l3 3-3 3" fill="none" stroke="#17b57f" stroke-width="1.5"/></svg></div>

<!-- Testimonial -->
<h2 class="abs testi-title">Chosen &amp; Trusted by 10,000+ Happy Guests</h2>
<div class="abs" style="left:541px;top:1472px;width:118px;height:1px;background:#6f8890"></div>
<div class="abs avatar" role="img" aria-label="Guest portrait photo"></div>
<p class="abs quote">"It is a long established fact that a reader will be distracted by the readable content of a page when looking at its layout. The point of using Lorem Ipsum is that it has a more-or-less normal distribution of letters, as opposed to using 'Content here, content here', making it look like readable English."</p>
<div class="abs" style="left:0;width:1200px;top:1675px;text-align:center;font-size:11px;color:var(--green)">Standard Chunk</div>
<div class="abs" style="left:0;width:1200px;top:1691px;text-align:center;font-size:11px;color:#fff">Lorem ipsum</div>
<span class="dot" style="left:563px"></span>
<span class="dot" style="left:579px;background:var(--green);border-color:var(--green)"></span>
<span class="dot" style="left:594px"></span>
<span class="dot" style="left:609px"></span>
<span class="dot" style="left:624px"></span>

<!-- Destinations -->
<h2 class="section-title" style="top:1849px">Explore Featured Destinations.</h2>
<div class="rule" style="top:1903px"></div>
<p class="lead" style="top:1897px">Explore villa holidays from destinations that will inspire you.</p>

<div class="dest" style="left:199px"><div class="img photo" style="position:relative;background:linear-gradient(180deg,#8fc3ea,#d9c8a8 45%,#b99a74 65%,#2aa2c4)" role="img" aria-label="Venice basilica on the Grand Canal"></div><div class="name">Italy</div><div class="tab"></div></div>
<div class="dest" style="left:405px"><div class="img photo" style="position:relative;background:linear-gradient(180deg,#4f9fdc,#9dcbe9 35%,#4c7a45 55%,#38c0c6 80%,#e5d6b0)" role="img" aria-label="Phuket limestone island with longtail boat"></div><div class="name" style="color:var(--orange)">Phuket</div><div class="tab"></div></div>
<div class="dest" style="left:611px"><div class="img photo" style="position:relative;background:linear-gradient(180deg,#2f84d2,#79b5e3 30%,#3f7a3a 55%,#2f5c2e 80%,#b76b4b)" role="img" aria-label="Koh Samui palm trees and resort pool"></div><div class="name">Koh Samui</div><div class="tab"></div></div>
<div class="dest" style="left:818px"><div class="img photo" style="position:relative;background:linear-gradient(180deg,#3b98e0,#8cc8ee 35%,#5fb7c7 60%,#c9b08a 80%,#e6e2da)" role="img" aria-label="Mauritius beach deck with palm trees and chairs"></div><div class="name">Mauritius</div><div class="tab"></div></div>

<div class="arrow-circle" style="left:312px;top:2246px"><svg viewBox="0 0 10 10"><path d="M6.5 2l-3 3 3 3" fill="none" stroke="#17b57f" stroke-width="1.5"/></svg></div>
<div class="arrow-circle" style="left:843px;top:2246px"><svg viewBox="0 0 10 10"><path d="M3.5 2l3 3-3 3" fill="none" stroke="#17b57f" stroke-width="1.5"/></svg></div>
<div class="btn btn-orange" style="left:557px;top:2246px;width:86px;height:24px">View All</div>

<!-- New villas -->
<div class="abs navy-band"></div>
<h2 class="section-title" style="top:2398px;color:#fff">New Villas and Vacation Rentals</h2>
<div class="rule" style="top:2451px;background:#51666e"></div>
<p class="lead" style="top:2446px;color:#fff">Lorem ipsum dolor sit amet, consectetur adipiscing elit, sed do eiusmod tempor incididunt ut labore et dolore magna aliqua.</p>

<div class="rental" style="left:311px">
  <div class="img photo" style="background:linear-gradient(180deg,#4f7a3a,#7ea35a 45%,#e6e4df 60%,#3fb3d6)" role="img" aria-label="Pool with parasols among olive trees"><span class="stars">★★★★★</span></div>
  <h3>Podere La Quercia</h3>
  <p class="desc">The owners offer a wide choice of Extra Services to make you feel welcome and to help you discover Tuscany in a "non touristy" way.</p>
  <div class="specs"><div><span>▣ Sleeps:</span>27</div><div><span>▤ Bedrooms:</span>10</div><div><span>▥ Bathrooms:</span>06</div><div><span>▦ Price:</span>€ 3400 per week</div></div>
</div>
<div class="rental" style="left:608px">
  <div class="img photo" style="background:linear-gradient(180deg,#5fa6df,#c3dcef 35%,#efe9e0 60%,#27a6d6)" role="img" aria-label="Modern white villa with large pool"><span class="stars">★★★★★</span></div>
  <h3>Agriturismo Il Colle</h3>
  <p class="desc">il casale è immerso nella campagna toscana ma a soli 3 km dal paese più vicino dove potete trovare tutti i negozi con le principali comodità.</p>
  <div class="specs"><div><span>▣ Sleeps:</span>07</div><div><span>▤ Bedrooms:</span>02</div><div><span>▥ Bathrooms:</span>02</div><div><span>▦ Price:</span>€ 3400 per week</div></div>
</div>
<div class="btn btn-green" style="left:311px;top:2827px;width:76px;height:23px">More Info</div>
<div class="btn btn-orange" style="left:398px;top:2827px;width:95px;height:23px">Book Now!</div>
<div class="btn btn-green" style="left:608px;top:2827px;width:76px;height:23px">More Info</div>
<div class="btn btn-orange" style="left:690px;top:2827px;width:95px;height:23px">Book Now!</div>
<div class="arrow-circle" style="left:298px;top:2569px;background:transparent"><svg viewBox="0 0 10 10"><path d="M6.5 2l-3 3 3 3" fill="none" stroke="#17b57f" stroke-width="1.5"/></svg></div>
<div class="arrow-circle" style="left:875px;top:2569px;background:transparent"><svg viewBox="0 0 10 10"><path d="M3.5 2l3 3-3 3" fill="none" stroke="#17b57f" stroke-width="1.5"/></svg></div>

<!-- Articles -->
<h2 class="section-title" style="top:2968px">Latest Articles</h2>
<div class="rule" style="top:3021px"></div>
<p class="lead" style="top:3016px">Lorem ipsum dolor sit amet, consectetur adipiscing elit, sed do eiusmod tempor incididunt ut labore et dolore magna aliqua.</p>

<div class="article" style="left:199px"><div class="img photo" style="position:relative;background:linear-gradient(160deg,#1f3a1c,#3f6b2e 50%,#e07a3a 70%,#2f4d24)" role="img" aria-label="Orange lily flower in a garden"></div>
  <div class="box"><div class="meta"><span style="color:var(--green)">▦</span> MARCH-20-2021 &nbsp; <span style="color:var(--green)">◷</span> 1:00PM - 7:00PM</div><h4>Contrary to popular belief, is lorem Ipsum is simply</h4><p>It is a long established fact that a reader will be distracted by the readable content of a page ...</p></div></div>
<div class="article" style="left:475px"><div class="img photo" style="position:relative;background:linear-gradient(180deg,#2f4a22,#6f8d4a 40%,#e8e6e0 60%,#7fa74d)" role="img" aria-label="White garden gazebo on a lawn"></div>
  <div class="box"><div class="meta"><span style="color:var(--green)">▦</span> MARCH-20-2021 &nbsp; <span style="color:var(--green)">◷</span> 1:00PM - 7:00PM</div><h4>Contrary to popular belief, is lorem Ipsum is simply</h4><p>It is a long established fact that a reader will be distracted by the readable content of a page ...</p></div></div>
<div class="article" style="left:750px"><div class="img photo" style="position:relative;background:linear-gradient(180deg,#2b4d22,#5d8b3c 50%,#7fae52)" role="img" aria-label="Garden trees and green lawn"></div>
  <div class="box"><div class="meta"><span style="color:var(--green)">▦</span> MARCH-20-2021 &nbsp; <span style="color:var(--green)">◷</span> 1:00PM - 7:00PM</div><h4>Contrary to popular belief, is lorem Ipsum is simply</h4><p>It is a long established fact that a reader will be distracted by the readable content of a page ...</p></div></div>
<div class="btn btn-green" style="left:237px;top:3334px;width:76px;height:23px">Read More</div>
<div class="btn btn-green" style="left:513px;top:3334px;width:76px;height:23px">Read More</div>
<div class="btn btn-green" style="left:788px;top:3334px;width:76px;height:23px">Read More</div>

<!-- Footer -->
<svg class="abs" style="left:0;top:3410px" width="1200" height="80" viewBox="0 0 1200 80" preserveAspectRatio="none"><path d="M0 20 C250 60 500 50 750 35 C950 22 1100 10 1200 12 L1200 80 L0 80Z" fill="#17b57f"/><path d="M0 52 C250 70 500 62 750 48 C950 36 1100 32 1200 34 L1200 80 L0 80Z" fill="#0f2b36"/></svg>
<div class="abs footer-dark" style="top:3480px;height:284px"></div>

<div class="foot-h" style="left:199px">Contact Us</div>
<div class="foot-t" style="left:199px;top:3556px;font-size:16px;color:var(--green)">Call: +39 055 4827190</div>
<div class="foot-t" style="left:199px;top:3578px;text-decoration:underline">info@lunquora.com</div>
<div class="foot-t" style="left:199px;top:3608px;line-height:16px">Address:<br>via delle Ginestre 7 50127 Borgo Verde,<br>Firenze (Italy)</div>

<div class="foot-h" style="left:475px">Quick Links</div>
<div class="foot-t" style="left:475px;top:3557px">Home<br>About Us<br>Special Offers<br>Experience<br>Blog<br>Contact Us</div>
<div class="foot-t" style="left:566px;top:3557px">Login<br>Register<br>Wish List<br>Privacy policy<br>Terms &amp; conditions</div>

<div class="foot-h" style="left:750px">Sign Up Newsletter</div>
<div class="foot-t" style="left:750px;top:3560px;line-height:13px;width:190px">Lorem ipsum dolor sit amet, sedtur consectetur adipiscing</div>
<div class="abs" style="left:750px;top:3597px;width:248px;height:30px;border-radius:16px;background:#1d3c47;color:#fff;font-size:9px;padding:9px 15px">Enter your email ...</div>
<div class="abs" style="left:970px;top:3601px;width:22px;height:22px;border-radius:50%;background:var(--orange);display:flex;align-items:center;justify-content:center"><svg width="10" height="10" viewBox="0 0 10 10"><path d="M1 1l8 4-8 4 2-4z" fill="none" stroke="#fff" stroke-width="1.2"/></svg></div>

<div class="abs bottom-bar"></div>
<div class="brand" style="left:202px;top:3725px;color:#fff;font-size:24px"><span class="brand-mark" style="width:24px;height:24px"></span>Villaroute</div>
<div class="foot-t" style="left:475px;top:3729px;font-size:9.5px">© 2021 <span style="color:var(--green)">Villaroute</span>. All Rights Reserved</div>
<span class="social" style="left:751px;top:3728px"></span>
<span class="social" style="left:781px;top:3728px;background:var(--green)"></span>
<span class="social" style="left:811px;top:3728px"></span>
<svg class="abs to-top" viewBox="0 0 24 24" role="img" aria-label="Back to top"><path d="M12 20V5M6 11l6-6 6 6" fill="none" stroke="#17b57f" stroke-width="2" stroke-linecap="round" stroke-linejoin="round"/></svg>

</body>
</html>
```